Vorlen - Customer Experience Software Company Web Design

*****UPDATE*****
We've been getting a lot of corporate designs through. Unfortunately this is not what we are looking for. We would like our brand to be more approachable and for the look and feel to to be a bit more fun.
Also the best designs we have received so far have followed the "less is more" approach. Im hoping any news designs will take these aspects into account.
*****************

Background:

Vorlen is a Customer Experience Technology company. We equip business and technology teams with the frameworks, tools and services to help them create compelling experiences for their customers.

Our flagship product - Vorlen CX is an open-source customer experience application framework – it enables organisation to build highly differentiated business applications to deliver compelling experiences to your customers.

Vorlen CX is designed for innovators who understand that unlocking opportunity in today’s competitive marketplace is driven by delivering a better customer experience.

Task:

We are looking for a web design (we need PSD, no HTML/CSS) for our company site through which to launch our customer experience framework product. The site will be also used as a support site, so the functional aspect of the site is as important as the visual impact for sales.

In order to help us conceptualise ideas and content we have drafted a temporary website using a standard wordpress theme (please see details below). Now we have a general idea of our requirements we like we would like to take it to the next level and get some designs with that professional edge.

Our target market are Enterprise organisations - that is senior members of the business & technology teams (Business General Managers, CTO’s, CIO’s, and Senior Architects and Senior Developers). We want something clean & fresh which is DIFFERENT from the typical corporate technology websites out there. We would like to be seen as more approachable than most large technology companies.

Words we would like to use to describe the finished design:
• Clean (we’re thinking white background with one or two key colours)
• Fresh
• Light
• Modern
• Less is more
• Web 2.0
• Fun but professional (aimed at Enterprise/Large organisations)
• Bold, clear call to action – e.g. Live Demo & Download
• Readable (but Sans Serif)

As we’re a Customer Experience company, the usability of the site is critical. The site must be functional, intuitive & easy to navigate. We want to keep the number of user clicks to the bare minimum possible.

Other aspects, which we would like to incorporate into the site
• Home Page banner slider
• Client logon
• Newsletter sign up
• Social media links – Friendwall, Netlinker (for starters)
• Rich footer links

Some websites we like
• http://brightpanelworks.example - clean, light, modern & intuitive
• http://www.tamsoledrik.example - bold, clear messaging
• http://www.opengridhub.example/markup/emblem - punchy, colourful
• http://postwren.example/ - modern, clear messaging, colourful, rich footer area

Target Market(s)

Enterprise organisations - that is senior members of the business & technology teams (Business General Managers, CTO’s, CIO’s, Senior Devs)

Industry/Entity Type

Business

Requirements
Must have
• - Design Specs: Accepted file formats: During the design phase adobe PSD or JPEG are OK (if you need to upload files), but for the handover we'll need PSD only with all the original layers.
- The width needs to be a size that will work with every size computer screen
- Need to use cross-platform compatible font
- The graphic elements used for the design must be copyright free

Current test site
- URL http://vorlen.example/wp-admin
- username: artmarket
- password: artmarket

IMPORTANT NOTE REGARDING OUR CURRENT TEST SITE:

This is a very basic version of a site to help us generate requirements. This design is only a starting point/input and is not locked in stone i.e. we do not simply want this site simply tweaked around the edges.

We are looking for you to use all of your graphic design skills and experience to create a truly awesome site design!

```html
<!DOCTYPE html>
<html lang="en">
<head>
<meta charset="utf-8">
<title>Vorlen.com — Home</title>
<link rel="stylesheet" href="https://fonts.googleapis.com/css2?family=Arimo:wght@400;700&family=PT+Sans:wght@400;700&display=swap">
<style>
  :root{
    --page:#f8f9fa;
    --panel:#eeeff0;
    --blue-top:#78c0ea;
    --blue-bottom:#3a8ccb;
    --blue-ink:#1d4f91;
    --nav-ink:#1e5aa6;
    --input-fill:#b8dcf1;
    --input-ink:#86b9d9;
    --body-ink:#9d9d9d;
    --link-ink:#5bb1e2;
    --rule:#d8dadc;
    --white:#ffffff;
  }
  *{box-sizing:border-box;margin:0;padding:0}
  html,body{width:1200px;height:1200px;overflow:hidden;background:var(--page)}
  body{position:relative;font-family:"Arimo",Arial,sans-serif}
  .abs{position:absolute}

  .main-nav a{
    position:absolute;top:0;height:67px;width:189px;
    display:flex;align-items:center;justify-content:center;
    font-family:"PT Sans",Tahoma,sans-serif;font-size:39px;color:var(--nav-ink);
    text-decoration:none;letter-spacing:-0.5px;
    background:linear-gradient(var(--blue-top),var(--blue-bottom));
    border-radius:0 0 9px 9px;
    box-shadow:0 2px 3px rgba(0,0,0,.15);z-index:3;
  }

  .hero-frame{left:127px;top:0;width:946px;height:384px;background:#d9d9d9;border-radius:0 0 10px 10px;box-shadow:0 0 6px rgba(0,0,0,.12)}
  .hero-slide{left:133px;top:0;width:934px;height:380px;border-radius:0 0 9px 9px;
    background:linear-gradient(115deg,#9a9a9a 0%,#e6e6e6 30%,#b5b5b5 55%,#3a3a3a 78%,#0c0c0c 100%)}
  .slider-arrow{top:164px;width:57px;height:60px}
  .slider-arrow.prev{left:57px}
  .slider-arrow.next{left:1091px}

  .login-pill{top:389px;height:55px;border-radius:18px;
    background:linear-gradient(var(--blue-top),var(--blue-bottom));display:flex;align-items:center}
  .login-pill label{font-family:"PT Sans",Tahoma,sans-serif;font-size:19px;color:var(--blue-ink)}
  .login-pill .field{position:absolute;top:8px;height:39px;border-radius:12px;background:var(--input-fill);
    display:flex;align-items:center;justify-content:center;font-size:15px;color:var(--input-ink)}

  .content-panel{left:133px;top:453px;width:934px;height:360px;border-radius:8px;
    background:linear-gradient(var(--panel) 0%,var(--panel) 40%,rgba(238,239,240,0) 100%)}
  .tool-box{top:460px;height:73px;border-radius:14px;background:linear-gradient(#fdfdfd,#e6e7e8);
    box-shadow:0 1px 3px rgba(0,0,0,.1);text-align:center}
  .tool-box h3{font-weight:400;font-size:18px;color:#6eb7e3;margin-top:8px;letter-spacing:-0.3px}
  .tool-box h3 b{color:var(--blue-ink);font-weight:400}
  .tool-box .field{position:absolute;left:10px;right:10px;bottom:10px;height:30px;border-radius:12px;background:#eef0f1;
    display:flex;align-items:center;justify-content:center;font-size:15px;color:#c3d7e6}
  .social-tile{top:460px;width:76px;height:73px;border-radius:9px;
    background:linear-gradient(#4aa2dc,#2d78bd);display:flex;align-items:center;justify-content:center;
    color:var(--white);font-size:13px;font-weight:700;text-decoration:none}

  .section-rule{left:153px;top:555px;width:894px;height:1px;background:var(--rule)}
  .site-title{left:0;top:555px;width:1160px;text-align:center;font-size:100px;letter-spacing:-2px;
    color:var(--blue-ink);text-shadow:1px 2px 2px rgba(0,0,0,.25)}
  .intro{left:173px;width:840px;text-align:center;font-size:15.5px;line-height:24px;color:var(--body-ink)}

  .footer-panel{left:133px;top:1011px;width:934px;height:189px;border-radius:10px 10px 0 0;
    background:linear-gradient(#eeeff0,#f6f7f8)}
  .footer-rule{left:160px;top:1068px;width:893px;height:1px;background:var(--rule)}
  .footer-col{top:1035px;width:200px;text-align:center}
  .footer-col h4{font-size:17px;font-weight:400;color:var(--blue-ink);height:33px}
  .footer-col ul{list-style:none;margin-top:20px}
  .footer-col li{font-size:16px;line-height:24px;color:var(--link-ink)}
</style>
</head>
<body>

<nav class="main-nav">
  <a href="#" style="left:200px">HOME</a>
  <a href="#" style="left:404px">SERVICES</a>
  <a href="#" style="left:607px">SUPPORT</a>
  <a href="#" style="left:811px">ABOUT</a>
</nav>

<div class="abs hero-frame"></div>
<div class="abs hero-slide" role="img" aria-label="Banner slide: black and white photo of a hand typing on a laptop keyboard"></div>
<svg class="abs slider-arrow prev" viewBox="0 0 57 60" aria-label="Previous slide"><polygon points="57,0 34,0 0,30 34,60 57,60 23,30" fill="#1e5aa6"/></svg>
<svg class="abs slider-arrow next" viewBox="0 0 57 60" aria-label="Next slide"><polygon points="0,0 23,0 57,30 23,60 0,60 34,30" fill="#1e5aa6"/></svg>

<form class="client-login">
  <div class="abs login-pill" style="left:133px;width:470px">
    <label style="margin-left:47px">Username:</label>
    <div class="field" style="left:168px;width:282px">Enter Username</div>
  </div>
  <div class="abs login-pill" style="left:597px;width:470px">
    <label style="margin-left:47px">Password:</label>
    <div class="field" style="left:162px;width:296px">Enter Password</div>
  </div>
</form>

<div class="abs content-panel"></div>

<div class="abs tool-box newsletter" style="left:140px;width:299px">
  <h3>SIGN UP FOR OUR <b>NEWSLETTER</b></h3>
  <div class="field">Enter Email Address</div>
</div>
<div class="abs tool-box site-search" style="left:461px;width:408px">
  <h3>SEARCH <b>VORLEN.COM</b></h3>
  <div class="field">Search...</div>
</div>
<a class="abs social-tile" href="#" style="left:887px">Netlinker</a>
<a class="abs social-tile" href="#" style="left:969px">Friendwall</a>

<div class="abs section-rule"></div>
<h1 class="abs site-title">VORLEN.COM</h1>

<p class="abs intro" style="top:670px">Lorem ipsum dolor sit amet, consectetur adipiscing elit. Nam at imperdiet ligula. Curabitur orci mi, tempor scelerisque ornare id, elementum sit amet quam. Donec eu orci elit, id imperdiet velit. Aliquam enim lorem, molestie sit amet blandit in, hendrerit id diam. Pellentesque habitant morbi tristique senectus et netus et malesuada fames ac turpis egestas. Nulla facilisi. Nullam porttitor eleifend justo at viverra. Nullam ligula felis, vulputate sed consectetur non, malesuada sed dolor. Nam nec elit ipsum. Duis et placerat ligula. Fusce aliquet lacinia hendrerit. Quisque sagittis bibendum risus at euismod.</p>
<p class="abs intro" style="top:838px">Nam a enim lectus. Etiam pellentesque vehicula erat in sodales. Ut porttitor placerat tortor sed ultrices. In et leo sit amet urna vulputate viverra a a mauris. Praesent fermentum, odio in vehicula mattis, nibh diam accumsan lorem, nec blandit tellus nunc sit amet magna. Ut sed sem vitae metus adipiscing rhoncus. Donec et erat eu orci feugiat tristique. Maecenas dolor ipsum, ultrices nec posuere et, ullamcorper posuere mi. Nam tincidunt risus vel orci porttitor lobortis.</p>

<footer>
  <div class="abs footer-panel"></div>
  <div class="abs footer-rule"></div>
  <div class="abs footer-col" style="left:171px"><h4>Services</h4><ul><li>link</li><li>link</li><li>link</li><li>link</li></ul></div>
  <div class="abs footer-col" style="left:500px"><h4>Support</h4><ul><li>link</li><li>link</li><li>link</li><li>link</li></ul></div>
  <div class="abs footer-col" style="left:840px"><h4>About</h4><ul><li>link</li><li>link</li><li>link</li><li>link</li></ul></div>
</footer>

</body>
</html>
```